stationary for hygienic company

We need a stationary design for hygienic company which provides public high end sanitary products and high end public lavatory.
We need a fresh and clean style stationary
we want the following things:
* logo (redesigned in eps/vector)
* Letterhead (with company details)
* letterhead (without company details)
* Business card
* note block
* ballpoint
* etcetera (a complete package)

```html
<!DOCTYPE html>
<html lang="fr">
<head>
<meta charset="utf-8">
<title>Velmora – Envelopes</title>
<link href="https://fonts.googleapis.com/css2?family=Jura:wght@400&display=swap" rel="stylesheet">
<style>
  :root {
    --page: #ffffff;
    --page-edge: #e4e4e4;
    --envelope: #ffffff;
    --envelope-edge: #c9c9c9;
    --taupe: #b5aba8;
    --mist: #e2dcd9;
    --window: #d4d5d7;
    --window-edge: #e9e9ea;
    --ink: #2b2b2b;
    --pink: #ff2e95;
    --navy: #00008b;
    --cyan: #00aeef;
    --graphite: #222022;
    --silver: #cfd0d2;
  }
  html, body {
    margin: 0;
    padding: 0;
    overflow: hidden;
    background: var(--page);
  }
  .sheet {
    position: relative;
    width: 849px;
    height: 1200px;
    box-sizing: border-box;
    border: 1px solid var(--page-edge);
    background: var(--page);
    overflow: hidden;
    font-family: "Jura", sans-serif;
  }
  .envelope {
    position: absolute;
    left: 115px;
    width: 621px;
    height: 294px;
    box-sizing: border-box;
    border: 1px solid var(--envelope-edge);
    border-radius: 2px;
    background: var(--envelope);
    overflow: hidden;
  }
  .envelope--window { top: 70px; background: linear-gradient(90deg, var(--envelope) 0, var(--envelope) 260px, var(--mist) 380px, var(--taupe) 520px, var(--taupe) 100%); }
  .envelope--colour { top: 436px; background: linear-gradient(90deg, var(--envelope) 0, var(--envelope) 260px, var(--mist) 400px); }
  .envelope--mono { top: 796px; }

  .address-window {
    position: absolute;
    left: 366px;
    top: 167px;
    width: 209px;
    height: 71px;
    box-sizing: border-box;
    border: 1px solid var(--window-edge);
    border-radius: 6px;
    background: var(--window);
  }

  .brand {
    position: absolute;
    display: flex;
    align-items: flex-start;
    gap: 10px;
    color: var(--ink);
  }
  .envelope--window .brand { left: 22px; top: 42px; }
  .envelope--colour .brand { left: 25px; top: 44px; }
  .envelope--mono .brand { left: 44px; top: 44px; }
  .brand__text { display: flex; flex-direction: column; align-items: flex-end; }
  .brand__name { font-size: 24px; line-height: 24px; letter-spacing: 0.2px; }
  .brand__tagline { font-size: 8.5px; line-height: 10px; margin-right: 8px; }
  .brand__mention { font-size: 4px; line-height: 6px; margin-right: 20px; }
  .brand__dot {
    width: 30px;
    height: 30px;
    margin-top: 4px;
    border-radius: 50%;
    background: var(--pink);
  }

  .decoration {
    position: absolute;
    top: 0;
    right: 0;
    height: 100%;
  }
  .decoration--colour {
    width: 268px;
    background: linear-gradient(135deg, var(--pink) 0%, var(--pink) 30%, var(--navy) 55%, var(--cyan) 100%);
    border-top-left-radius: 60px 300px;
  }
  .decoration--mono {
    width: 190px;
    background: linear-gradient(135deg, #77787b 0%, var(--silver) 40%, var(--graphite) 65%, #939496 100%);
    border-top-left-radius: 60px 300px;
  }
</style>
</head>
<body>
<main class="sheet">

  <section class="envelope envelope--window">
    <div class="brand">
      <div class="brand__text">
        <span class="brand__name">Velmora</span>
        <span class="brand__tagline">Boutique Hygienique</span>
        <span class="brand__mention">Marque déposée</span>
      </div>
      <span class="brand__dot"></span>
    </div>
    <div class="address-window"></div>
  </section>

  <section class="envelope envelope--colour">
    <div class="brand">
      <div class="brand__text">
        <span class="brand__name">Velmora</span>
        <span class="brand__tagline">Boutique Hygienique</span>
        <span class="brand__mention">Marque déposée</span>
      </div>
      <span class="brand__dot"></span>
    </div>
    <div class="decoration decoration--colour" role="img" aria-label="Large decorative brand graphic in pink, navy and cyan"></div>
  </section>

  <section class="envelope envelope--mono">
    <div class="brand">
      <div class="brand__text">
        <span class="brand__name">Velmora</span>
        <span class="brand__tagline">Boutique Hygienique</span>
        <span class="brand__mention">Marque déposée</span>
      </div>
      <span class="brand__dot"></span>
    </div>
    <div class="decoration decoration--mono" role="img" aria-label="Large decorative brand graphic in greyscale tones"></div>
  </section>

</main>
</body>
</html>
```